Buff & Gleam

polished concrete and epoxy coatings flooring company

Target Market(s)

Industrial commercial

Industry/Entity Type

Industrial flooring contractor

Contact Information for Business Card

POLISHED CONCRETE • EPOXY COATING • TERRAZZO RESTORATION • SHOT BLASTING • SURFACE PREPARATION • JOINT FILLING • TILE/ CARPET /GLUE REMOVAL

Colors
0054AA
0677BA
7BADD7
CADEEF
E8F1F8

Requirements
Must have
• email buffandgleamfloors@mailbrook.example Address 47215 Tallowmere Rd, Brackenford, OH 44710. Name Ray Tulvin. Services Polished concrete- Epoxy Coatings- Terrazzo restoration-surface preparation- safety striping- joint filling- tile/ carpet/ glue removal phone number 555-700-3926 email buffandgleamfloors.example
Nice to have
• Instagram Facebook logo maybe smaller in the corner

```html
<!DOCTYPE html>
<html lang="en">
<head>
<meta charset="utf-8">
<title>Buff &amp; Gleam — Business Card</title>
<link rel="stylesheet" href="https://fonts.googleapis.com/css2?family=Oswald:wght@500;600&family=Roboto:wght@400;500&display=swap">
<style>
  :root {
    --page-bg: #2b2c2e;
    --card-bg: #1d1e20;
    --brand-blue: #0677ba;
    --edge-blue: #0054aa;
    --text-white: #ffffff;
    --rule: #d9d9d9;
  }
  * { box-sizing: border-box; margin: 0; padding: 0; }
  html, body { width: 1200px; height: 840px; overflow: hidden; }
  body {
    background: var(--page-bg);
    font-family: "Roboto", Arial, sans-serif;
    color: var(--text-white);
    display: flex;
    flex-direction: column;
    align-items: center;
    justify-content: center;
    gap: 50px;
  }
  .card {
    position: relative;
    width: 600px;
    height: 340px;
    background: var(--card-bg);
    border-radius: 22px;
    border-bottom: 5px solid var(--edge-blue);
    border-left: 3px solid var(--edge-blue);
    overflow: hidden;
  }

  /* shared wordmark */
  .wordmark {
    font-family: "Roboto", Arial, sans-serif;
    font-weight: 500;
    color: var(--text-white);
    letter-spacing: 2px;
    line-height: 1;
    white-space: nowrap;
  }
  .tagline {
    font-family: "Oswald", Arial, sans-serif;
    font-weight: 500;
    color: var(--brand-blue);
    text-transform: uppercase;
    letter-spacing: 0.5px;
  }

  /* front: services */
  .card-front .brand {
    position: absolute;
    top: 42px; left: 0; right: 0;
    text-align: center;
  }
  .card-front .wordmark { font-size: 50px; }
  .card-front .tagline { font-size: 17px; margin-top: 8px; }
  .services-heading {
    position: absolute;
    top: 165px; left: 40px; right: 40px;
    display: flex; align-items: center; gap: 14px;
  }
  .services-heading .rule { flex: 1; height: 1px; background: var(--rule); }
  .services-pill {
    font-family: "Oswald", Arial, sans-serif;
    font-weight: 600;
    font-size: 20px;
    letter-spacing: 1px;
    background: var(--brand-blue);
    color: var(--text-white);
    border-radius: 20px;
    padding: 2px 20px 4px;
  }
  .services-list {
    position: absolute;
    top: 212px; left: 20px; right: 20px;
    text-align: center;
    font-size: 17px;
    line-height: 1.55;
  }
  .services-list .dot { color: var(--brand-blue); margin: 0 4px; }

  /* back: contact */
  .card-back .brand {
    position: absolute;
    top: 40px; right: 40px;
    text-align: right;
  }
  .card-back .wordmark { font-size: 42px; }
  .card-back .tagline { font-size: 15px; margin-top: 8px; }
  .divider {
    position: absolute;
    top: 178px; left: 40px; right: 40px;
    height: 1px; background: var(--rule);
  }
  .person-name {
    position: absolute;
    top: 140px; left: 40px;
    font-weight: 500;
    font-size: 26px;
    color: var(--brand-blue);
    text-transform: uppercase;
  }
  .contact-list {
    position: absolute;
    top: 200px; left: 40px;
    list-style: none;
    font-size: 16px;
    line-height: 1.75;
  }
  .contact-list li { display: flex; align-items: center; gap: 10px; }
  .contact-list svg { width: 17px; height: 17px; fill: var(--brand-blue); flex: none; }
  .address {
    position: absolute;
    top: 196px; right: 40px;
    text-align: right;
    font-size: 16px;
    line-height: 1.45;
    font-style: normal;
  }
</style>
</head>
<body>

  <section class="card card-front" aria-label="Business card front">
    <div class="brand">
      <div class="wordmark">BUFF &amp; GLEAM</div>
      <div class="tagline">Innovative Concrete Flooring</div>
    </div>
    <div class="services-heading">
      <span class="rule"></span>
      <span class="services-pill">SERVICES</span>
      <span class="rule"></span>
    </div>
    <p class="services-list">
      <span class="dot">•</span>Polished concrete <span class="dot">•</span>Epoxy Coatings<br>
      <span class="dot">•</span>Terrazzo restoration <span class="dot">•</span>surface preparation <span class="dot">•</span>safety striping<br>
      <span class="dot">•</span>joint filling <span class="dot">•</span>tile/ carpet/ glue removal
    </p>
  </section>

  <section class="card card-back" aria-label="Business card back">
    <div class="brand">
      <div class="wordmark">BUFF &amp; GLEAM</div>
      <div class="tagline">Innovative Concrete Flooring</div>
    </div>
    <div class="person-name">Ray Tulvin</div>
    <div class="divider"></div>
    <ul class="contact-list">
      <li>
        <svg viewBox="0 0 24 24" aria-hidden="true"><path d="M6.6 10.8a15 15 0 0 0 6.6 6.6l2.2-2.2a1 1 0 0 1 1-.25 11.4 11.4 0 0 0 3.6.57 1 1 0 0 1 1 1V20a1 1 0 0 1-1 1A17 17 0 0 1 3 4a1 1 0 0 1 1-1h3.5a1 1 0 0 1 1 1c0 1.25.2 2.45.57 3.57a1 1 0 0 1-.25 1z"/></svg>
        555-700-3926
      </li>
      <li>
        <svg viewBox="0 0 24 24" aria-hidden="true"><path d="M3 5h18a1 1 0 0 1 1 1v12a1 1 0 0 1-1 1H3a1 1 0 0 1-1-1V6a1 1 0 0 1 1-1zm9 7.2L20 7H4z"/></svg>
        buffandgleamfloors@mailbrook.example
      </li>
      <li>
        <svg viewBox="0 0 24 24" aria-hidden="true"><path d="M12 2a10 10 0 1 0 0 20 10 10 0 0 0 0-20zm6.9 6h-3a15 15 0 0 0-1.3-3.9A8 8 0 0 1 18.9 8zM12 4c.8 1.1 1.5 2.5 1.9 4h-3.8c.4-1.5 1.1-2.9 1.9-4zM4.3 14a8 8 0 0 1 0-4h3.4a16 16 0 0 0 0 4zm.8 2h3a15 15 0 0 0 1.3 3.9A8 8 0 0 1 5.1 16zm3-8h-3a8 8 0 0 1 4.3-3.9A15 15 0 0 0 8.1 8zM12 20c-.8-1.1-1.5-2.5-1.9-4h3.8c-.4 1.5-1.1 2.9-1.9 4zm2.3-6H9.7a14 14 0 0 1 0-4h4.6a14 14 0 0 1 0 4zm.3 5.9a15 15 0 0 0 1.3-3.9h3a8 8 0 0 1-4.3 3.9zm1.7-5.9a16 16 0 0 0 0-4h3.4a8 8 0 0 1 0 4z"/></svg>
        buffandgleamfloors.example
      </li>
    </ul>
    <address class="address">
      47215 Tallowmere Rd<br>
      Brackenford, OH 44710
    </address>
  </section>

</body>
</html>
```